Copper Lantern Gatherings need a stand out marketing flyer.

Copper Lantern Gatherings is a company that runs empowerment retreats and bespoke corporate training in creating positive change.
We would like an A5 flyer that is 2 sided. the reverse side of the flyer we would like some of our testimonial quotes.

The flyer should be punchy and not too heavy with wordy detail but have enough detail so people can see what we offer. Encouraging people to contact us to find out more

Our empowerment retreats help people to live without limits, be fierce and wild, be creative and courageous, be fearless and free.
Leave behind
- lack of self esteem
- lack of personal power
- lack of focus
- old fears and beliefs
- overwhelm
Find new
- confidence
- personal empowerment
- commitment
- courage
- resilience

Contact details:
website: www.copperlanterngatherings.example.co.uk
email: info@copperlanterngatherings.example.com
Rebecca Thornby Tel: 07700 900 318
Joanna Pelling Tel: 07700 900 752

You can use as much of the detail above in your design as you would like..
I attach our logos. you can pick which ever design you prefer to work with. I have also attached a file that contains the testimonials for the reverse of the slide. I've also attached a few pictures but these aren't necessary in your design they are just an option/idea for you to consider. You can use alternative pictures should you wish to.

Details for our up and coming events can be found on our website

```html
<!DOCTYPE html>
<html lang="en">
<head>
<meta charset="utf-8">
<title>Copper Lantern Gatherings – Empowerment Retreats Flyer</title>
<link rel="stylesheet" href="https://fonts.googleapis.com/css2?family=Cinzel:wght@400;700&family=Lato:ital,wght@0,400;0,700;1,400&family=Roboto+Slab:wght@700&display=swap">
<style>
  :root {
    --page-bg: #d9d9d9;
    --ink-dark: #1c1c1e;
    --panel-dark: #232326;
    --blue-deep: #0b4fb3;
    --blue-main: #1277e0;
    --blue-bright: #27a6f2;
    --blue-text: #1c5fb8;
    --white: #ffffff;
    --grey-light: #ececec;
    --grey-mid: #b9b9b9;
    --chalk: #8f8f8f;
    --chalk-strip: #7a7a7a;
    --chalk-initial: #2b2b2b;
    --body-text: #222222;
  }
  * { box-sizing: border-box; margin: 0; padding: 0; }
  html, body { width: 1200px; height: 902px; overflow: hidden; }
  body { background: var(--page-bg); position: relative; font-family: "Lato", sans-serif; }

  .flyer {
    position: absolute;
    width: 437px;
    height: 613px;
    transform: scale(0.97);
    transform-origin: top left;
    overflow: hidden;
    box-shadow: 0 6px 14px rgba(0,0,0,0.25);
  }
  .flyer-front { left: 121px; top: 99px; background: var(--panel-dark); }
  .flyer-back { left: 632px; top: 226px; background: var(--grey-light); }
  .flyer-art { position: absolute; inset: 0; width: 437px; height: 613px; }
  .abs { position: absolute; }

  /* Front */
  .photo-label {
    left: 36px; top: 100px;
    font: 700 18px/1 "Lato", sans-serif;
    letter-spacing: 5px; color: var(--white);
  }
  .brand-name {
    font-family: "Cinzel", serif; font-weight: 700;
    color: var(--blue-main); text-align: center;
  }
  .front-brand { left: 300px; top: 52px; width: 118px; font-size: 14px; line-height: 1.25; }
  .retreat-title {
    left: 228px; top: 322px; width: 209px; text-align: center;
    font: 700 19px/24px "Cinzel", serif; color: var(--blue-text);
  }
  .retreat-title .first { font-size: 22px; }
  .help-badge {
    left: 216px; top: 402px; width: 206px; height: 34px;
    border-radius: 5px; border: 2px solid #0d3f86;
    background: linear-gradient(180deg, #8fd0ff 0%, #2f8ee8 55%, #1560c4 100%);
    font: 700 22px/30px "Cinzel", serif; color: #0c2550;
    text-align: center; letter-spacing: 0.5px;
  }
  .promise-list { left: 228px; top: 444px; width: 209px; list-style: none; text-align: center; }
  .promise-list li {
    font: italic 400 14px/1 "Lato", sans-serif; color: var(--body-text);
    height: 32px; padding-top: 13px; position: relative;
  }
  .promise-list li::before {
    content: ""; position: absolute; left: 50%; top: 2px;
    width: 8px; height: 8px; margin-left: -4px;
    border-right: 2px solid var(--blue-main); border-bottom: 2px solid var(--blue-main);
    transform: rotate(45deg);
  }
  .change-box {
    left: 30px; width: 160px; border: 1.5px solid #e6e6e6; border-radius: 10px;
    padding: 12px 0 0 22px;
  }
  .change-box.leave { top: 308px; height: 88px; }
  .change-box.find { top: 416px; height: 88px; }
  .change-tab {
    left: 35px; width: 145px; height: 14px; text-align: center;
    background: linear-gradient(180deg, #6fc3ff, #1a6fd8);
    font: 400 9px/14px "Cinzel", serif; letter-spacing: 1px; color: #0a2148;
  }
  .change-tab.leave { top: 301px; }
  .change-tab.find { top: 409px; }
  .change-box ul { list-style: none; }
  .change-box li {
    font: 400 8.6px/14px "Lato", sans-serif; color: var(--white);
    position: relative; padding-left: 13px;
  }
  .change-box li::before {
    content: ""; position: absolute; left: 0; top: 4px; width: 6px; height: 6px;
    border-radius: 50%; background: var(--blue-bright);
  }
  .contact-cta {
    left: 24px; top: 521px;
    font: 700 9px/1 "Cinzel", serif; letter-spacing: 1px; color: var(--ink-dark);
  }
  .contact-people { left: 26px; top: 542px; color: var(--white); font: 400 10px/12.5px "Lato", sans-serif; }
  .contact-links { left: 26px; top: 572px; color: var(--white); font: 400 7.8px/11px "Lato", sans-serif; list-style: none; }
  .contact-links li { display: flex; align-items: center; gap: 5px; }
  .contact-links svg { width: 7px; height: 7px; flex: none; }

  /* Back */
  .fear-strip { left: 52px; top: 28px; width: 46px; height: 190px; background: var(--chalk-strip); opacity: 0.8; }
  .fear-row {
    position: absolute; left: 52px;
    font: 700 40px/1 "Roboto Slab", serif; white-space: nowrap; color: var(--chalk);
  }
  .fear-row .initial { display: inline-block; width: 46px; text-align: center; color: var(--chalk-initial); }
  .back-brand { left: 246px; top: 160px; width: 130px; font-size: 15px; line-height: 1.25; }
  .quote-mark { left: 34px; top: 290px; font: 700 96px/1 Georgia, serif; color: var(--grey-mid); }
  .testimonials { left: 42px; top: 373px; width: 372px; list-style: none; }
  .testimonials li { font: 400 7.8px/11px "Lato", sans-serif; color: var(--body-text); margin-bottom: 12px; }
  .web-band {
    left: 0; top: 562px; width: 437px; height: 25px;
    background: linear-gradient(90deg, var(--blue-deep), var(--blue-main) 50%, var(--blue-deep));
    color: var(--white); text-align: center; font: 700 11.5px/25px "Lato", sans-serif;
  }
</style>
</head>
<body>

<section class="flyer flyer-front" aria-label="Flyer front">
  <svg class="flyer-art" viewBox="0 0 437 613">
    <defs>
      <linearGradient id="front-dark" x1="0" y1="0" x2="1" y2="1">
        <stop offset="0" stop-color="#2c2c30"/><stop offset="1" stop-color="#141416"/>
      </linearGradient>
      <linearGradient id="hands-photo" x1="0" y1="0" x2="0.4" y2="1">
        <stop offset="0" stop-color="#6b5a4e"/><stop offset="0.45" stop-color="#b9876b"/><stop offset="1" stop-color="#6f9a3a"/>
      </linearGradient>
      <linearGradient id="hands-fade" x1="0" y1="0" x2="1" y2="0">
        <stop offset="0.7" stop-color="#232326" stop-opacity="0"/><stop offset="1" stop-color="#232326"/>
      </linearGradient>
      <linearGradient id="figure-photo" x1="0" y1="0" x2="0" y2="1">
        <stop offset="0" stop-color="#9fc4dd"/><stop offset="0.55" stop-color="#d8b48c"/><stop offset="1" stop-color="#f4f1ec"/>
      </linearGradient>
      <linearGradient id="panel-white" x1="0" y1="0" x2="0" y2="1">
        <stop offset="0" stop-color="#ffffff"/><stop offset="1" stop-color="#e9e9e9"/>
      </linearGradient>
      <linearGradient id="blue-sweep" x1="0" y1="0" x2="1" y2="0.3">
        <stop offset="0" stop-color="#0a4fb0"/><stop offset="0.5" stop-color="#1b86e8"/><stop offset="1" stop-color="#0b55bd"/>
      </linearGradient>
      <linearGradient id="blue-foot" x1="0" y1="0" x2="1" y2="0">
        <stop offset="0" stop-color="#0b5fcc"/><stop offset="1" stop-color="#2aaaf3"/>
      </linearGradient>
      <linearGradient id="left-panel" x1="0" y1="0" x2="1" y2="0">
        <stop offset="0" stop-color="#3a3a3e"/><stop offset="1" stop-color="#1c1c1f"/>
      </linearGradient>
    </defs>
    <rect width="437" height="613" fill="url(#front-dark)"/>
    <rect x="0" y="0" width="300" height="215" fill="url(#hands-photo)" role="img" aria-label="Photo of many hands stacked together in a circle over grass"/>
    <rect x="0" y="0" width="300" height="215" fill="url(#hands-fade)"/>
    <rect x="0" y="285" width="240" height="235" fill="url(#left-panel)"/>
    <rect x="0" y="530" width="437" height="83" fill="url(#blue-foot)"/>
    <path d="M228,232 Q228,200 262,197 L437,180 L437,600 L280,600 Q240,598 232,560 Z" fill="url(#panel-white)"/>
    <path d="M228,312 L228,232 Q228,200 262,197 L437,180 L437,312 Z" fill="url(#figure-photo)" role="img" aria-label="Photo of a hand offering a key to a small wooden figure"/>
    <rect x="0" y="514" width="240" height="26" fill="#ffffff"/>
    <path d="M0,146 C120,148 200,212 300,188 C360,174 400,156 437,148 L437,160 C400,168 360,186 300,200 C200,224 120,160 0,158 Z" fill="#ffffff"/>
    <path d="M0,158 C120,160 200,224 300,200 C360,186 400,168 437,160 L437,180 C380,190 300,196 262,200 C232,206 222,250 200,270 C180,288 150,292 120,292 L0,292 Z" fill="url(#blue-sweep)"/>
  </svg>

  <div class="abs photo-label">EMPOWERMENT</div>
  <div class="abs brand-name front-brand">Copper Lantern Gatherings</div>

  <h1 class="abs retreat-title"><span class="first">Our</span><br>Empowerment<br>Retreats</h1>
  <div class="abs help-badge">HELP PEOPLE</div>
  <ul class="abs promise-list">
    <li>To live without limits</li>
    <li>Be fierce and wild</li>
    <li>Be creative and courageous</li>
    <li>Be fearless and free</li>
  </ul>

  <div class="abs change-box leave">
    <ul>
      <li>Lack of self esteem</li>
      <li>Lack of personal power</li>
      <li>Lack of focus</li>
      <li>Old fears and beliefs</li>
      <li>Overwhelm</li>
    </ul>
  </div>
  <div class="abs change-tab leave">LEAVE BEHIND</div>

  <div class="abs change-box find">
    <ul>
      <li>Confidence</li>
      <li>Personal empowerment</li>
      <li>Commitment</li>
      <li>Courage</li>
      <li>Resilience</li>
    </ul>
  </div>
  <div class="abs change-tab find">FIND NEW</div>

  <div class="abs contact-cta">CONTACT US TO FIND OUT MORE.....</div>
  <div class="abs contact-people">
    Rebecca Thornby Tel: 07700 900 318<br>
    Joanna Pelling Tel: 07700 900 752
  </div>
  <ul class="abs contact-links">
    <li><svg viewBox="0 0 10 10"><rect x="0.5" y="2" width="9" height="6" fill="none" stroke="#fff" stroke-width="1"/><path d="M0.5,2 L5,6 L9.5,2" fill="none" stroke="#fff" stroke-width="1"/></svg>www.copperlanterngatherings.example.co.uk</li>
    <li><svg viewBox="0 0 10 10"><circle cx="5" cy="5" r="4.3" fill="none" stroke="#fff" stroke-width="1"/><path d="M0.7,5 H9.3 M5,0.7 V9.3" stroke="#fff" stroke-width="0.8"/></svg>info@copperlanterngatherings.example.com</li>
  </ul>
</section>

<section class="flyer flyer-back" aria-label="Flyer back">
  <svg class="flyer-art" viewBox="0 0 437 613">
    <defs>
      <radialGradient id="chalkboard" cx="0.5" cy="0.4" r="0.8">
        <stop offset="0" stop-color="#2e2e2e"/><stop offset="1" stop-color="#161616"/>
      </radialGradient>
      <linearGradient id="back-grey" x1="0" y1="0" x2="0" y2="1">
        <stop offset="0" stop-color="#d4d4d4"/><stop offset="0.4" stop-color="#f4f4f4"/><stop offset="1" stop-color="#dcdcdc"/>
      </linearGradient>
      <linearGradient id="back-blue" x1="0" y1="0" x2="1" y2="0">
        <stop offset="0" stop-color="#0a4fb0"/><stop offset="0.6" stop-color="#1a86ea"/><stop offset="1" stop-color="#0b58c0"/>
      </linearGradient>
    </defs>
    <rect width="437" height="613" fill="url(#back-grey)"/>
    <path d="M0,0 H437 V222 C300,236 150,214 0,238 Z" fill="url(#chalkboard)"/>
    <path d="M0,238 C150,214 300,236 437,222 L437,232 C300,246 150,226 0,248 Z" fill="#ffffff"/>
    <path d="M0,248 C150,226 300,246 437,232 L437,330 C400,362 330,366 270,348 C180,320 80,252 0,262 Z" fill="url(#back-blue)"/>
  </svg>

  <div class="abs fear-strip" aria-hidden="true"></div>
  <div class="abs fear-stack" aria-label="Face Everything And Rise" style="left:0;top:0">
    <div class="fear-row" style="top:52px"><span class="initial">F</span>ACE</div>
    <div class="fear-row" style="top:92px"><span class="initial">E</span>VERYTHING</div>
    <div class="fear-row" style="top:134px"><span class="initial">A</span>ND</div>
    <div class="fear-row" style="top:174px"><span class="initial">R</span>ISE</div>
  </div>
  <div class="abs brand-name back-brand">Copper Lantern Gatherings</div>

  <div class="abs quote-mark">&ldquo;</div>
  <ul class="abs testimonials">
    <li>Do not hesitate, just book it!  It will transform and enhance your life.</li>
    <li>If you have a chance to do it then do it, it's one of the best experience of my life.</li>
    <li>The most wonderful weekend of self-discovery and would recommend it to everyone.</li>
    <li>I've met the most amazing people and feel like I am well equipped with the tools now to help myself physically and mentally.  The best self-care I've ever invested in.</li>
    <li>It's changed my life, given me perspective and time to develop myself.  I've met the most amazing people and learnt so much.  It's worth every penny.</li>
    <li>I can't thank Copper Lantern enough for the tools they have metaphorically equipped me with.  They are amazing at what they do.</li>
  </ul>
  <div class="abs web-band">www.copperlanterngatherings.example.co.uk</div>
</section>

</body>
</html>
```